Business Card Design Project

Hi. We need a new business card for Brightfield Partners, a consultancy that helps people with online marketing strategy and solutions.

We have a new logo and now need the info presented - front and back of business card.

FRONT

Logo

Online strategy, consulting and coaching
Varlo Admarket consulting
Search Engine Optimisation
Internet Lead Generation
Domain name broking

BACK

Tom Bradwell-Jones
+ 61 83215 9076
+ 61 (0) 418 536 207
tom@brightfieldpartners.com.au
www.brightfieldpartners.com.au

Talkora: tombradwelljones
PO Box 312, South Perth, Western Australia 6951

Target Market(s)

Business owners, corporates

Industry/Entity Type

Marketing

Requirements
Must have
• double sided
size: 86 x 54mm
supplied as one pdf with crop marks shown (+- 1mm, with 2-3 mm bleed)

```html
<!DOCTYPE html>
<html lang="en">
<head>
<meta charset="utf-8">
<title>Brightfield Partners – Business Card</title>
<link rel="stylesheet" href="https://fonts.googleapis.com/css2?family=Open+Sans:wght@400;600;700;800&display=swap">
<style>
  :root {
    --brand-blue: #2a5a93;
    --brand-blue-dark: #1f4a7d;
    --brand-orange: #e5801c;
    --panel-white: #f7f7f7;
    --panel-grey: #e4e4e4;
    --text-grey: #6b6b6b;
    --page-bg: #2b2b2b;
    --white: #ffffff;
  }
  * { margin: 0; padding: 0; box-sizing: border-box; }
  html, body {
    width: 1200px; height: 900px; overflow: hidden;
    background: var(--page-bg);
    font-family: "Open Sans", Arial, sans-serif;
  }
  .canvas {
    width: 1200px; height: 900px;
    display: flex; align-items: center; justify-content: center; gap: 40px;
  }
  .card {
    position: relative;
    width: 540px; height: 340px;
    overflow: hidden;
    box-shadow: 0 12px 30px rgba(0,0,0,0.45);
  }

  /* Services side */
  .card--services {
    background: var(--brand-blue);
    padding: 22px;
  }
  .services-panel {
    width: 100%; height: 100%;
    border-radius: 30px;
    background: linear-gradient(160deg, var(--panel-white) 0%, var(--panel-grey) 100%);
    padding: 40px 0 0 92px;
  }
  .brand-lockup {
    display: flex; align-items: center; gap: 10px;
  }
  .brand-mark {
    width: 30px; height: 30px; border-radius: 50%;
    background: var(--brand-orange); flex: none;
  }
  .brand-name {
    font-weight: 800; color: var(--brand-blue-dark);
    font-size: 26px; letter-spacing: -0.3px; line-height: 1.1;
  }
  .brand-domain {
    margin: 6px 0 0 40px;
    font-size: 10px; letter-spacing: 1.6px; color: var(--text-grey);
  }
  .services-list {
    list-style: none; margin-top: 22px;
    font-size: 14px; line-height: 1.6; color: var(--text-grey);
  }

  /* Contact side */
  .card--contact { background: var(--brand-blue); }
  .contact-shapes { position: absolute; inset: 0; }
  .contact-details {
    position: absolute; left: 18px; top: 30px; width: 180px;
    color: var(--white);
  }
  .contact-name {
    font-weight: 700; font-size: 17px; margin-bottom: 14px; white-space: nowrap;
  }
  .contact-line { font-size: 11.5px; line-height: 1.55; white-space: nowrap; }
  .contact-line + .contact-gap { height: 8px; }
  .contact-logo {
    position: absolute; left: 232px; top: 110px;
  }
  .contact-logo .brand-name { font-size: 24px; }
  .contact-web {
    position: absolute; right: 24px; bottom: 20px;
    color: #dfe8f3; font-size: 13px; letter-spacing: 0.3px;
  }
</style>
</head>
<body>
<main class="canvas">

  <section class="card card--services" aria-label="Card front">
    <div class="services-panel">
      <div class="brand-lockup">
        <span class="brand-mark"></span>
        <span class="brand-name">Brightfield Partners</span>
      </div>
      <p class="brand-domain">brightfieldpartners.com.au</p>
      <ul class="services-list">
        <li>Online strategy, consulting &amp; coaching</li>
        <li>Varlo Admarket consulting</li>
        <li>Search Engine Optimisation</li>
        <li>Internet Lead Generation</li>
        <li>Domain name broking</li>
      </ul>
    </div>
  </section>

  <section class="card card--contact" aria-label="Card back">
    <svg class="contact-shapes" width="540" height="340" viewBox="0 0 540 340" aria-hidden="true">
      <defs>
        <linearGradient id="panelFill" x1="0" y1="0" x2="1" y2="1">
          <stop offset="0" stop-color="#ffffff"/>
          <stop offset="1" stop-color="#e6e6e6"/>
        </linearGradient>
      </defs>
      <path d="M205 0 H540 V288 L335 250 H250 Q205 250 205 205 Z" fill="url(#panelFill)"/>
      <path d="M420 0 H540 V110 Z" fill="var(--brand-orange)"/>
    </svg>

    <div class="contact-details">
      <p class="contact-name">Tom Bradwell-Jones</p>
      <p class="contact-line">+ 61 83215 9076</p>
      <p class="contact-line">+ 61 (0) 418 536 207</p>
      <p class="contact-line">tom@brightfieldpartners.com.au</p>
      <div class="contact-gap"></div>
      <p class="contact-line">PO Box 312, South Perth,</p>
      <p class="contact-line">Western Australia 6951</p>
    </div>

    <div class="contact-logo brand-lockup">
      <span class="brand-mark"></span>
      <span class="brand-name">Brightfield Partners</span>
    </div>

    <p class="contact-web">www.brightfieldpartners.com.au</p>
  </section>

</main>
</body>
</html>
```